BROVA Website Redesign - More modern look & feel

I will upload high resolution copies of the BROVA logo tomorrow
Please make website responsive/mobile friendly
Use simple and clean black & white, easy to read text, color transitions & translucent, shadows, reflections/metallic
Alternate between white and black backgrounds from section to section but start with white background at top of fold/hero section
Freeze top bar & change to dark when scrolling down
If possible, have site convert to black background when consumer using dark mode on their phone or browser
Use high quality images of various types of business payments, in-store and online
Make sure photos are inclusive of race & sex/gender and show payments & business interaction
Use a high quality image of a website payment checkout screen
Use clear banner for logos under hero section
CTA at each section (bold caps with bright green)
Use only one shade of green
Use consistent font/text
Use Brova building image at bottom in get started section
US businesses
Fintech (financial technology) / merchant services
1 page

```html
<!DOCTYPE html>
<html lang="en">
<head>
<meta charset="utf-8">
<title>BROVA — Payments Simplified</title>
<link href="https://fonts.googleapis.com/css2?family=Poppins:wght@300;400;500;600;700&display=swap" rel="stylesheet">
<style>
:root{
  --ink:#000;
  --dark:#1f1f1f;
  --light:#ededed;
  --white:#fff;
  --teal:#16a7c3;
  --teal-deep:#0d5f73;
  --green:#22d46a;
  --text:#222;
  --muted:#555;
}
*{box-sizing:border-box;margin:0;padding:0}
html,body{width:1200px;height:4550px;overflow:hidden}
body{position:relative;font-family:'Poppins',sans-serif;color:var(--text);background:var(--white)}
.abs{position:absolute}
/* header */
.topbar{left:0;top:0;width:1200px;height:95px;background:var(--ink)}
.brand{left:74px;top:22px;color:var(--white);font-weight:300;font-size:40px;letter-spacing:34px;line-height:50px}
.nav{top:25px;height:45px;display:flex;align-items:center;color:var(--white);font-size:14px;letter-spacing:.5px}
.pill{top:25px;height:45px;border-radius:23px;display:flex;align-items:center;justify-content:center;font-size:14px;color:var(--white)}
.pill.login{left:876px;width:96px;background:var(--teal)}
.pill.start{left:986px;width:139px;background:var(--green);color:var(--ink);font-weight:700}
/* hero */
.hero-photo{left:0;top:95px;width:1200px;height:720px;background:linear-gradient(100deg,#f3f2ef 0%,#e9e6e1 40%,#d8d4cd 62%,#d9a23a 78%,#c9c5bd 100%)}
.hero-title{left:70px;top:290px;font-size:44px;font-weight:700;color:var(--ink)}
.hero-sub{left:70px;top:350px;font-size:21px;font-weight:600;color:var(--teal)}
.hero-body{left:70px;top:392px;width:440px;font-size:18px;line-height:33px;color:var(--ink)}
.btn{display:flex;align-items:center;justify-content:center;border-radius:26px;font-size:15px;font-weight:500}
.btn.cta{background:var(--green);color:var(--ink);font-weight:700;text-transform:uppercase;letter-spacing:.8px;font-size:14px}
.btn.outline-ink{border:1.5px solid var(--ink);color:var(--ink)}
.logo-banner{left:0;top:585px;width:1200px;height:74px;background:rgba(255,255,255,.45);display:flex;align-items:center;justify-content:center;gap:56px}
.logo-slot{width:150px;height:34px;border-radius:6px;background:rgba(0,0,0,.16)}
.chat{left:1057px;top:744px;width:88px;height:88px;border-radius:50%;background:var(--teal);box-shadow:0 0 0 8px rgba(22,167,195,.35)}
/* solutions */
.solutions{left:0;top:800px;width:1200px;height:1000px;background:var(--dark)}
.h-section{width:1200px;left:0;text-align:center;font-size:44px;font-weight:600;color:var(--white)}
.sol-photo{border-radius:26px;box-shadow:-6px 6px 0 #000,0 10px 24px rgba(0,0,0,.5)}
.sol-photo.sub{left:80px;top:965px;width:445px;height:380px;background:linear-gradient(150deg,#6a6f72,#bfc3c4 45%,#8a8f90)}
.sol-photo.risk{left:677px;top:1402px;width:448px;height:392px;background:radial-gradient(circle at 50% 45%,#6fd3f5 0%,#1a6fb8 30%,#0a2a5c 70%,#061733 100%)}
.timeline{left:599px;top:965px;width:2px;height:462px;background:var(--teal-deep)}
.dot{width:40px;height:40px;border-radius:50%;background:#0c3e4c;left:580px}
.dot::after{content:"";position:absolute;left:11px;top:11px;width:18px;height:18px;border-radius:50%;background:var(--teal)}
.sol-title{font-size:38px;font-weight:500;color:var(--white)}
.sol-sub{font-size:17px;color:var(--teal)}
.sol-body{width:455px;font-size:15px;letter-spacing:.3px;line-height:32.5px;color:#e4e4e4}
/* features */
.features{left:0;top:1900px;width:1200px;height:740px;background:var(--light)}
.card{background:var(--white);border-radius:6px;text-align:center;padding-top:36px}
.card svg{display:block;margin:0 auto}
.card h3{font-size:21px;font-weight:500;color:var(--ink);margin-top:18px}
.card p{font-size:14px;line-height:28.5px;color:var(--muted);margin-top:8px;letter-spacing:.2px}
/* pricing */
.pricing{left:0;top:2620px;width:1200px;height:780px;background:var(--dark)}
.plan{top:2797px;width:318px;height:432px;background:var(--white);border-radius:0 28px 0 28px;box-shadow:13px 13px 0 #000;padding:20px 22px 0}
.plan .name{text-align:center;font-size:19px;font-weight:500;color:var(--ink)}
.plan .price{text-align:center;font-size:40px;font-weight:700;color:var(--ink);line-height:52px}
.plan .price sup{font-size:22px;font-weight:500;vertical-align:16px}
.plan .price span{font-size:27px;font-weight:300}
.plan ul{list-style:none;margin-top:16px}
.plan li{font-size:15px;letter-spacing:.2px;line-height:23px;margin-bottom:9px;color:var(--text)}
.plan li b{font-weight:600}
.plan .btn{width:160px;height:46px;margin:10px auto 0}
.arrow{top:2975px}
/* faq */
.faq-title{left:0;width:1200px;top:3476px;text-align:center;font-size:36px;font-weight:500;color:var(--ink)}
.faq{width:512px;height:46px;border:1px solid #ccc;display:flex;align-items:center;justify-content:space-between;padding:0 16px;font-size:14px;color:var(--ink)}
.faq b{color:var(--teal);font-size:22px;font-weight:600}
/* footer */
.footer{left:0;top:3890px;width:1200px;height:660px;background:var(--ink);color:var(--white)}
.f-brand{left:74px;top:4120px;font-size:36px;font-weight:300;letter-spacing:30px;color:var(--white)}
.f-h{font-size:21px;font-weight:600;color:var(--white)}
.f-list{list-style:none;font-size:14px;line-height:38px;color:#cfcfcf;letter-spacing:.3px}
.email{left:74px;top:4255px;width:244px;height:51px;border:1.5px solid #ddd;border-radius:26px;padding-left:24px;display:flex;align-items:center;font-size:14px;color:#ddd}
.subscribe-btn{left:74px;top:4318px;width:244px;height:50px;border-radius:26px;background:var(--teal);display:flex;align-items:center;justify-content:center;font-size:15px;font-weight:500;color:var(--white)}
.rule{left:0;top:4452px;width:1200px;height:1px;background:#333}
.copyright{left:74px;top:4482px;font-size:14px;color:#cfcfcf}
.social{top:4488px;width:22px;height:22px;border-radius:4px;background:var(--white)}
</style>
</head>
<body>

<!-- Header -->
<div class="abs topbar"></div>
<div class="abs brand">BROVA</div>
<div class="abs nav" style="left:555px">SOLUTIONS</div>
<div class="abs nav" style="left:680px">PRICING</div>
<div class="abs nav" style="left:779px">CONTACT</div>
<div class="abs pill login">LOG IN</div>
<div class="abs pill start">GET STARTED</div>

<!-- Hero -->
<div class="abs hero-photo" role="img" aria-label="Woman in a yellow sweater on a sofa paying online with her phone and a card"></div>
<h1 class="abs hero-title">Payments Simplified.</h1>
<div class="abs hero-sub">Accept payments your way.</div>
<p class="abs hero-body">Transparent pricing+ quick &amp; easy setup for all types of businesses.</p>
<div class="abs btn cta" style="left:74px;top:475px;width:161px;height:48px">Get Started</div>
<div class="abs btn outline-ink" style="left:251px;top:475px;width:198px;height:48px">Free to Get Started</div>

<div class="abs logo-banner" role="img" aria-label="Banner of partner logos">
  <div class="logo-slot"></div><div class="logo-slot"></div><div class="logo-slot"></div><div class="logo-slot"></div><div class="logo-slot"></div>
</div>

<!-- Solutions -->
<div class="abs solutions"></div>
<svg class="abs" style="left:0;top:670px" width="1200" height="140" viewBox="0 0 1200 140">
  <path d="M0 45 C150 20 260 30 400 70 C520 105 620 80 760 110 C900 135 1050 140 1200 105 L1200 140 L0 140 Z" fill="#1f1f1f"/>
</svg>
<div class="abs chat">
  <svg width="88" height="88" viewBox="0 0 88 88">
    <rect x="26" y="28" width="36" height="26" rx="8" fill="none" stroke="#fff" stroke-width="3"/>
    <path d="M34 54 L30 63 L42 54" fill="#fff"/>
    <circle cx="37" cy="41" r="3" fill="#fff"/><circle cx="51" cy="41" r="3" fill="#fff"/>
  </svg>
</div>
<h2 class="abs h-section" style="top:850px">Solutions</h2>

<div class="abs timeline"></div>
<div class="abs dot" style="top:1005px"></div>
<div class="abs dot" style="top:1407px"></div>

<div class="abs sol-photo sub" role="img" aria-label="Laptop showing a subscription plan page while a hand holds a payment card"></div>
<h3 class="abs sol-title" style="left:673px;top:998px">Subscription</h3>
<div class="abs sol-sub" style="left:673px;top:1060px">Sed ut perspiciatis unde omnis iste natus error</div>
<p class="abs sol-body" style="left:673px;top:1099px">Sed ut perspiciatis unde omnis iste natus error sit voluptatem accusantium doloremque laudantium, totam rem aperiam, eaque ipsa quae ab illo inventore veritatis et quasi architecto beatae vitae dicta sunt explicabo. Nemo enim ipsam voluptatem .</p>
<div class="abs btn cta" style="left:673px;top:1288px;width:161px;height:49px">Get Started</div>

<h3 class="abs sol-title" style="left:74px;top:1410px">High Risk</h3>
<div class="abs sol-sub" style="left:74px;top:1470px">Sed ut perspiciatis unde omnis iste natus error</div>
<p class="abs sol-body" style="left:74px;top:1509px">Sed ut perspiciatis unde omnis iste natus error sit voluptatem accusantium doloremque laudantium, totam rem aperiam, eaque ipsa quae ab illo inventore veritatis et quasi architecto beatae vitae dicta sunt explicabo. Nemo enim ipsam voluptatem .</p>
<div class="abs btn cta" style="left:74px;top:1700px;width:161px;height:49px">Get Started</div>
<div class="abs sol-photo risk" role="img" aria-label="Hand turning a glowing risk dial from min to max"></div>

<!-- Features -->
<div class="abs features"></div>
<svg class="abs" style="left:0;top:1795px" width="1200" height="160" viewBox="0 0 1200 160">
  <path d="M0 0 L1200 0 L1200 50 C900 80 700 140 500 140 C350 140 200 70 0 10 Z" fill="#1f1f1f"/>
  <path d="M0 10 C200 70 350 140 500 140 C700 140 900 80 1200 50 L1200 160 L0 160 Z" fill="#ededed"/>
</svg>

<div class="abs card" style="left:148px;top:1965px;width:292px;height:250px">
  <svg width="76" height="60" viewBox="0 0 76 60" fill="none" stroke="#16a7c3" stroke-width="2">
    <circle cx="26" cy="30" r="10"/><circle cx="26" cy="30" r="18" stroke-dasharray="6 4"/>
    <circle cx="56" cy="18" r="6"/><circle cx="56" cy="18" r="11" stroke-dasharray="4 3"/>
    <circle cx="58" cy="44" r="5"/><circle cx="58" cy="44" r="9" stroke-dasharray="4 3"/>
  </svg>
  <h3>Simple Setup</h3>
  <p>Just 3 steps to get you through<br>the initial process.</p>
</div>
<div class="abs card" style="left:457px;top:2098px;width:292px;height:250px">
  <svg width="60" height="60" viewBox="0 0 60 60" fill="none" stroke="#16a7c3" stroke-width="2">
    <rect x="6" y="28" width="10" height="26"/>
    <path d="M16 30 L28 12 C30 6 36 6 36 14 L34 24 L50 24 C55 24 56 30 52 32 C56 34 55 40 51 40 C54 42 53 48 49 48 C52 50 50 56 46 56 L16 54"/>
  </svg>
  <h3>Fast Approval</h3>
  <p>99.9% Account Approval Rate<br>24-48 Hour Approval Time</p>
</div>
<div class="abs card" style="left:763px;top:1965px;width:292px;height:250px">
  <svg width="72" height="60" viewBox="0 0 72 60" fill="none" stroke="#16a7c3" stroke-width="2">
    <rect x="4" y="14" width="64" height="34" rx="2"/><rect x="10" y="20" width="52" height="22" stroke-dasharray="3 3"/>
    <circle cx="36" cy="31" r="8"/><path d="M36 26 V36"/>
  </svg>
  <h3>Cost Saving</h3>
  <p>Better Rates vs Your Current<br>Provider Cash Discounts for<br>Low-Risk / Retail Merchants.</p>
</div>
<div class="abs card" style="left:148px;top:2231px;width:292px;height:250px">
  <svg width="60" height="60" viewBox="0 0 60 60" fill="none" stroke="#16a7c3" stroke-width="2">
    <circle cx="30" cy="30" r="26"/><circle cx="30" cy="30" r="20"/>
    <path d="M38 20 C34 16 22 17 23 25 C24 32 38 28 38 36 C38 44 25 44 21 39"/>
  </svg>
  <h3>No Application Fee</h3>
  <p>Free Consultation<br>Free Rate Review<br>No Hidden Fees</p>
</div>
<div class="abs card" style="left:763px;top:2231px;width:292px;height:250px">
  <svg width="68" height="60" viewBox="0 0 68 60" fill="none" stroke="#16a7c3" stroke-width="2">
    <path d="M6 26 C6 14 18 8 30 8 C42 8 52 14 52 26 C52 36 42 42 30 42 C26 42 22 41 19 40 L8 46 L12 37 C8 34 6 30 6 26 Z"/>
    <path d="M54 22 C60 26 62 32 60 38 L64 48 L54 43 C48 46 40 46 34 44"/>
  </svg>
  <h3>Customer Care</h3>
  <p>You will have customer service<br>teams who are ready to talk 24<br>hours a day, 365 days a year.</p>
</div>

<!-- Pricing -->
<div class="abs pricing"></div>
<svg class="abs" style="left:0;top:2560px" width="1200" height="80" viewBox="0 0 1200 80">
  <path d="M0 55 C200 70 350 70 480 50 C640 25 760 10 900 30 C1020 48 1120 60 1200 55 L1200 80 L0 80 Z" fill="#1f1f1f"/>
</svg>
<h2 class="abs h-section" style="top:2690px;font-size:38px;font-weight:500">Pricing Plan</h2>

<svg class="abs arrow" style="left:38px" width="24" height="40" viewBox="0 0 24 40"><path d="M20 4 L6 20 L20 36" fill="none" stroke="#fff" stroke-width="3"/></svg>
<svg class="abs arrow" style="left:1138px" width="24" height="40" viewBox="0 0 24 40"><path d="M4 4 L18 20 L4 36" fill="none" stroke="#fff" stroke-width="3"/></svg>

<div class="abs plan" style="left:74px">
  <div class="name">Subscripton</div>
  <div class="price"><sup>$</sup>19<span>/m</span></div>
  <ul>
    <li><b>High Risk -</b> Interchange<br>cost-plus 2%</li>
    <li><b>Convenience Fees -</b> Pass your fees to your customers</li>
    <li><b>Quote -</b> Will beat your current rates or offer (documented) Bundle</li>
    <li><b>Bundle -</b> Buy more, save more</li>
  </ul>
  <div class="btn cta">Get Started</div>
</div>
<div class="abs plan" style="left:434px">
  <div class="name">Subscripton</div>
  <div class="price"><sup>$</sup>49<span>/m</span></div>
  <ul>
    <li><b>High Risk -</b> Interchange<br>cost-plus 2%</li>
    <li><b>Convenience Fees -</b> Pass your fees to your customers</li>
    <li><b>Quote -</b> Will beat your current rates or offer (documented) Bundle</li>
    <li><b>Bundle -</b> Buy more, save more</li>
  </ul>
  <div class="btn cta">Get Started</div>
</div>
<div class="abs plan" style="left:795px">
  <div class="name">Subscripton</div>
  <div class="price"><sup>$</sup>99<span>/m</span></div>
  <ul>
    <li><b>High Risk -</b> Interchange<br>cost-plus 2%</li>
    <li><b>Convenience Fees -</b> Pass your fees to your customers</li>
    <li><b>Quote -</b> Will beat your current rates or offer (documented) Bundle</li>
    <li><b>Bundle -</b> Buy more, save more</li>
  </ul>
  <div class="btn cta">Get Started</div>
</div>

<!-- FAQ -->
<svg class="abs" style="left:0;top:3300px" width="1200" height="120" viewBox="0 0 1200 120">
  <path d="M0 100 C150 60 300 20 480 30 C640 40 760 80 900 70 C1020 60 1120 40 1200 30 L1200 120 L0 120 Z" fill="#fff"/>
</svg>
<h2 class="abs faq-title">FAQ's</h2>
<div class="abs faq" style="left:74px;top:3567px">Excepteur sint occaecat cupidatat non proident.? <b>+</b></div>
<div class="abs faq" style="left:615px;top:3567px">Excepteur sint occaecat cupidatat non proident.? <b>+</b></div>
<div class="abs faq" style="left:74px;top:3628px">Excepteur sint occaecat cupidatat non proident.? <b>+</b></div>
<div class="abs faq" style="left:615px;top:3628px">Excepteur sint occaecat cupidatat non proident.? <b>+</b></div>
<div class="abs faq" style="left:74px;top:3690px">Excepteur sint occaecat cupidatat non proident.? <b>+</b></div>
<div class="abs faq" style="left:615px;top:3690px">Excepteur sint occaecat cupidatat non proident.? <b>+</b></div>
<div class="abs faq" style="left:74px;top:3751px">Excepteur sint occaecat cupidatat non proident.? <b>+</b></div>
<div class="abs faq" style="left:615px;top:3751px">Excepteur sint occaecat cupidatat non proident.? <b>+</b></div>
<div class="abs faq" style="left:74px;top:3815px">Excepteur sint occaecat cupidatat non proident.? <b>+</b></div>
<div class="abs faq" style="left:615px;top:3815px">Excepteur sint occaecat cupidatat non proident.? <b>+</b></div>

<!-- Footer -->
<div class="abs footer"></div>
<svg class="abs" style="left:0;top:3880px" width="1200" height="110" viewBox="0 0 1200 110">
  <path d="M0 30 C120 50 220 90 360 95 C520 100 640 60 800 40 C960 20 1100 10 1200 5 L1200 0 L0 0 Z" fill="#fff"/>
</svg>
<div class="abs f-brand">BROVA</div>
<div class="abs f-h" style="left:72px;top:4206px;font-size:22px">Subscribe</div>
<div class="abs email">Enter Email</div>
<div class="abs subscribe-btn">Subscribtion</div>

<div class="abs f-h" style="left:388px;top:4130px">Solutions</div>
<ul class="abs f-list" style="left:388px;top:4168px">
  <li>Subscription</li><li>High Risk</li><li>Convenience</li><li>Fees</li><li>Crypto</li>
</ul>
<ul class="abs f-list" style="left:523px;top:4168px">
  <li>Card Issuing</li><li>BPO &amp; 3PL</li><li>Global &amp; APMs</li><li>Gateway</li>
</ul>

<div class="abs f-h" style="left:703px;top:4130px">Pricing</div>
<ul class="abs f-list" style="left:703px;top:4168px">
  <li>Subscription</li><li>High Risk</li><li>Quote</li>
</ul>
<div class="abs f-h" style="left:703px;top:4288px">Get Started</div>
<ul class="abs f-list" style="left:703px;top:4326px">
  <li>Registration</li><li>Application</li><li>Partners</li>
</ul>

<div class="abs f-h" style="left:928px;top:4130px">Contact</div>
<ul class="abs f-list" style="left:928px;top:4168px">
  <li>Sales</li><li>Why</li><li>Partners</li><li>Pay 101 Support</li><li>FAQ</li>
</ul>

<div class="abs rule"></div>
<div class="abs copyright">© 2022 Brova Inc.&nbsp; All Rights Reserved.</div>
<div class="abs social" style="left:966px" aria-label="Social link"></div>
<div class="abs social" style="left:1010px" aria-label="Social link"></div>
<div class="abs social" style="left:1056px" aria-label="Social link"></div>
<div class="abs social" style="left:1102px" aria-label="Social link"></div>

</body>
</html>
```